Flyer Design Project

We need a flyer design for our company based in Ontario, Canada called CrateLoop. We rent out plastic reusable moving boxes. Please visit Crateloop.ca to find out more information about our company. We are looking for a creative, clean, and fun flyer design. The flyers purpose is to share with others what services CrateLoop offers as well as how convient our service is while still being cheaper than cardboard boxes.

Industry/Entity Type

Plastic

```html
<!DOCTYPE html>
<html lang="en">
<head>
<meta charset="utf-8">
<title>CrateLoop Flyer</title>
<link rel="stylesheet" href="https://fonts.googleapis.com/css2?family=Didact+Gothic&family=Montserrat:wght@700&display=swap">
<style>
  :root {
    --page-bg: #e4e4e4;
    --paper: #ffffff;
    --brand-green: #80bf00;
    --ink: #1e1e1e;
    --divider: #b9b9b9;
    --crate-green-light: #9ad11c;
    --crate-green-dark: #6aa300;
    --cardboard-light: #d9b98e;
    --cardboard-dark: #b58e5e;
  }
  * { margin: 0; padding: 0; box-sizing: border-box; }
  html, body {
    width: 1200px; height: 900px; overflow: hidden;
    background: var(--page-bg);
    font-family: "Didact Gothic", "Century Gothic", sans-serif;
  }
  .flyer {
    position: absolute; left: 332px; top: 58px;
    width: 534px; height: 757px;
    background: var(--paper);
  }
  .brand { position: absolute; left: 23px; top: 25px; display: flex; align-items: center; gap: 8px; }
  .brand-mark { width: 44px; height: 44px; background: var(--brand-green); }
  .brand-name {
    font-family: "Montserrat", sans-serif; font-weight: 700;
    font-size: 30px; color: var(--ink); letter-spacing: -0.5px;
  }
  .phone {
    position: absolute; left: 24px; top: 101px;
    font-size: 18px; color: var(--brand-green);
  }
  .service-areas {
    position: absolute; left: 34px; top: 132px;
    list-style: none; font-size: 10px; line-height: 13.55px; color: var(--ink);
  }
  .photo-crates {
    position: absolute; left: 183px; top: 258px; width: 282px; height: 160px;
    background: linear-gradient(160deg, var(--crate-green-light), var(--crate-green-dark));
    border-radius: 6px;
  }
  .photo-wardrobe-box {
    position: absolute; left: 336px; top: 50px; width: 178px; height: 236px;
    background: linear-gradient(160deg, var(--cardboard-light), var(--cardboard-dark));
    border-radius: 4px;
  }
  .steps {
    position: absolute; left: 16px; top: 458px; width: 510px;
    display: grid; grid-template-columns: 177px 147px 186px;
    color: var(--brand-green); text-align: center;
  }
  .step-title { font-size: 13.5px; height: 30px; }
  .step-text { font-size: 12.5px; line-height: 18px; padding-top: 0; }
  .step + .step .step-text { border-left: 1px solid var(--divider); }
  .icon-band {
    position: absolute; left: 0; top: 563px; width: 534px; height: 95px;
    background: var(--brand-green);
  }
  .icon-badge {
    position: absolute; top: 6px; width: 83px; height: 83px;
    background: var(--paper); border-radius: 50%;
    display: flex; align-items: center; justify-content: center;
  }
  .tagline {
    position: absolute; left: 0; top: 692px; width: 522px; text-align: center;
    font-size: 19px; color: var(--brand-green);
  }
</style>
</head>
<body>
<main class="flyer">
  <header class="brand">
    <span class="brand-mark"></span>
    <span class="brand-name">CrateLoop</span>
  </header>
  <p class="phone">1-800-555-0142</p>

  <ul class="service-areas">
    <li>Alvinston</li><li>Arkona</li><li>Bothwell</li><li>Brigden</li>
    <li>Brights Grove</li><li>Chatham</li><li>Delaware</li><li>Dresden</li>
    <li>Forest</li><li>Glencoe</li><li>Inwood</li><li>Kerwood</li>
    <li>Lambton Shores</li><li>Melbourne</li><li>Mt Brydges</li><li>Oil City</li>
    <li>Oil Springs</li><li>Petrolia</li><li>Pt Edward</li><li>Sarnia</li>
    <li>Strathroy</li><li>Wallaceburg</li><li>Watford</li><li>Wyoming</li>
  </ul>

  <div class="photo-wardrobe-box" role="img" aria-label="Photo of an open cardboard wardrobe box with clothes on hangers"></div>
  <div class="photo-crates" role="img" aria-label="Photo of two green plastic stackable moving crates with lids"></div>

  <section class="steps">
    <div class="step">
      <h3 class="step-title" style="font-weight:400">Step 1</h3>
      <p class="step-text">We deliver your moving boxes<br>right to your front door<br>(unless you prefer side door).</p>
    </div>
    <div class="step">
      <h3 class="step-title" style="font-weight:400">Step 2</h3>
      <p class="step-text">Pack it up! Our boxes<br>protect your belongings<br>and make stacking safe.</p>
    </div>
    <div class="step">
      <h3 class="step-title" style="font-weight:400">Step 3</h3>
      <p class="step-text">Once you're unpacked<br>we'll come by your new home<br>and collect the moving boxes.</p>
    </div>
  </section>

  <section class="icon-band">
    <div class="icon-badge" style="left:70px">
      <svg width="54" height="40" viewBox="0 0 54 40" aria-label="Delivery truck">
        <rect x="1" y="2" width="32" height="26" fill="#1e1e1e"/>
        <path d="M35 10h10l7 9v9H35z" fill="#1e1e1e"/>
        <path d="M38 13h6l4 6h-10z" fill="#fff"/>
        <circle cx="11" cy="32" r="6" fill="#1e1e1e" stroke="#fff" stroke-width="2"/>
        <circle cx="43" cy="32" r="6" fill="#1e1e1e" stroke="#fff" stroke-width="2"/>
      </svg>
    </div>
    <div class="icon-badge" style="left:225px">
      <svg width="54" height="50" viewBox="0 0 54 50" aria-label="Open box" fill="none" stroke="#1e1e1e" stroke-width="3" stroke-linejoin="round">
        <path d="M10 18l17-6 17 6v26l-17 5-17-5z"/>
        <path d="M10 18l17 6 17-6M27 24v25"/>
        <path d="M10 18L3 8l16-6 8 10M44 18l7-10-16-6-8 10"/>
      </svg>
    </div>
    <div class="icon-badge" style="left:381px">
      <svg width="50" height="46" viewBox="0 0 50 46" aria-label="House">
        <path d="M25 3L3 22h6v22h32V22h6z" fill="none" stroke="#1e1e1e" stroke-width="4" stroke-linejoin="round"/>
        <rect x="21" y="27" width="9" height="17" fill="#1e1e1e"/>
        <rect x="33" y="8" width="5" height="8" fill="#1e1e1e"/>
      </svg>
    </div>
  </section>

  <p class="tagline">Plastic, stackable, eco-friendly moving boxes</p>
</main>
</body>
</html>
```